Website design for a construction company

The logo and the copies of all the 3 pages are attached below. I don't have a preference in colors but I would ideally like to use the colors on my logo, dark teal (secondary) and copper (primary).

Company Name: Torvane Group

Location: London, UK

Business Overview:

Torvane Group is a comprehensive construction company based in London, specializing in a wide range of construction services. We cater to various sectors, providing services including electrical work, painting and decorating, plastering, plumbing, carpentry, kitchen and bathroom installations, loft conversions, and extensions. Our team is known for its skilled craftsmanship, attention to detail, and commitment to quality.

What "TORVANE" stands for:

Our company name, 'TORVANE', is derived from Torvanos, the ancient Greek god of craftsmen, blacksmiths, artisans, sculptors, metals, metallurgy, fire, and volcanoes. Torvanos was renowned in mythology for his incredible skill in crafting and creating, making him the patron of all craftsmen and artisans. His name is synonymous with the mastery of artisanship and the creation of wondrous, enduring works.

In choosing 'TORVANE' as our name, we embody the spirit and skills of Torvanos. It reflects our commitment to craftsmanship, excellence, and durability in the field of construction. Just as Torvanos was known for his meticulous work, precision, and innovative creations, our company strives to uphold these qualities in every project we undertake.

Our name is a constant reminder of our dedication to quality, innovation, and the art of building. It symbolizes our endeavor to achieve the highest standards in construction, much like Torvanos did in his timeless creations. In essence, 'TORVANE' is not just our name; it's a representation of our ethos and the high standards we set for ourselves in the construction industry.

Target Audience:

Our primary audience includes homeowners, real estate developers, and commercial clients in London seeking reliable, high-quality construction services.

Unique Selling Points:

Diverse Range of Services: Offering a one-stop solution for all construction needs.

Certified and Experienced: Professional team with a strong focus on delivering certified and compliant work, particularly in electrical services.

Client-Centric Approach: Emphasizing client satisfaction, we tailor our services to meet the unique needs and visions of our clients.

Quality and Reliability: Commitment to high-quality materials, skilled workmanship, and delivering projects on time and within budget.

Website Requirements:

Clean, professional design reflecting the quality and reliability of our services.

User-friendly navigation to easily access information about our services, portfolio, company background, and contact details.

Portfolio section showcasing our past projects with placeholders for images and descriptions.

Integration of a contact form, map for our location, and links to our social media accounts.

Mobile-responsive design to ensure accessibility across various devices.

Purpose of the Website:
The website aims to:

Establish an online presence and credibility in the construction industry.

Provide an informative resource about our services and past projects to potential clients.

Facilitate easy communication and inquiries through an integrated contact system.

Tone and Style:

Professional, informative, and welcoming. The website should convey trustworthiness and expertise in the construction field.

Target Market(s)

homeowners, real estate developers, and commercial clients

Industry/Entity Type

Construction

Number of Pages Required

3 page

Colors

Designer to choose colors to be used in the design.

```html
<!DOCTYPE html>
<html lang="en">
<head>
<meta charset="utf-8">
<title>Torvane Group – Construction in London</title>
<link rel="stylesheet" href="https://fonts.googleapis.com/css2?family=Nunito:wght@400;600;700;800;900&family=Cormorant+Garamond:wght@500&family=Inter:wght@400;500;600&family=Montserrat:wght@400;500&display=swap">
<style>
:root{
  --teal:#1b8c84;
  --copper:#c4902f;
  --copper-btn:#b8832f;
  --navy:#0d2c8b;
  --leaf:#2a9a6b;
  --ink:#1c1c1c;
  --muted:#8a8a8a;
  --page:#f6f6f6;
  --white:#ffffff;
}
*{box-sizing:border-box;margin:0;padding:0}
html,body{width:1200px;height:3071px;overflow:hidden}
body{position:relative;background:var(--page);font-family:"Inter",sans-serif;color:var(--ink)}
.abs{position:absolute}
.brand{display:flex;align-items:center;gap:9px}
.brand-mark{width:30px;height:30px;background:var(--teal)}
.brand-name{font-family:"Nunito",sans-serif;font-weight:700;font-size:27px;color:var(--ink);letter-spacing:.5px}
/* header */
.site-header{left:0;top:0;width:1200px;height:118px;background:var(--page)}
.site-header .brand{position:absolute;left:86px;top:42px}
.main-nav{position:absolute;top:48px;left:450px}
.main-nav a{position:absolute;white-space:nowrap;font-family:"Montserrat",sans-serif;font-size:16.5px;color:var(--ink);text-decoration:none}
/* hero */
.hero{left:0;top:118px;width:1200px;height:517px;background:var(--white)}
.hero-eyebrow{left:83px;top:70px;font-family:"Cormorant Garamond",serif;font-weight:500;font-size:26px;color:var(--leaf)}
.hero-title{left:83px;top:108px;font-family:"Nunito",sans-serif;font-weight:900;font-size:49px;line-height:71px;color:var(--navy)}
.hero-text{left:83px;top:250px;width:500px;font-family:"Montserrat",sans-serif;font-size:18.5px;line-height:29px;color:#2a2a2a}
.btn-outline{left:82px;top:404px;width:130px;height:48px;border:2px solid var(--leaf);border-radius:3px;color:var(--leaf);font-size:14px;display:flex;align-items:center;justify-content:center}
.hero-art{left:652px;top:20px;width:476px;height:474px;background:linear-gradient(160deg,#eef1f1,#dfe8e6 55%,#cfe3df);border-radius:6px}
/* why */
.deco-left{left:0;top:660px}
.deco-right{left:0;top:635px}
.why-photo{left:86px;top:747px;width:421px;height:374px;border-radius:12px;background:linear-gradient(135deg,#7fe0cf 0%,#22c3b3 40%,#0d5e57 70%,#163a39 100%)}
.stat-box{left:56px;top:930px;width:192px;height:164px;background:var(--white);padding:10px}
.stat-inner{width:100%;height:100%;background:var(--teal);color:var(--white);text-align:center;padding-top:20px}
.stat-inner .num{font-family:"Nunito",sans-serif;font-size:28px;font-weight:600;margin-top:8px}
.stat-inner .num sup{font-size:16px}
.stat-inner .lbl{font-size:11px;margin-top:8px}
.eyebrow{font-family:"Nunito",sans-serif;font-weight:700;font-size:17px;color:var(--copper)}
.sec-title{font-family:"Nunito",sans-serif;font-weight:700;font-size:28px;line-height:38px;color:var(--ink)}
.sec-title em{font-style:normal;color:var(--teal)}
.why-head{left:555px;top:716px}
.why-head .sec-title{margin-top:6px}
.feature-card{width:266px;height:142px;background:var(--white);border-radius:6px;box-shadow:0 4px 14px rgba(0,0,0,.08);padding:18px 14px 0 14px;display:flex;gap:14px}
.feature-card .ico{flex:0 0 40px;height:40px;display:flex;align-items:center;justify-content:center}
.feature-card h3{font-family:"Nunito",sans-serif;font-weight:700;font-size:17px;color:var(--teal);margin-bottom:10px}
.feature-card p{font-size:10.5px;line-height:15.5px;color:#333}
/* services */
.svc-head{left:60px;top:1240px;width:612px;text-align:center}
.svc-grid{left:69px;top:1374px;display:grid;grid-template-columns:repeat(4,128px);column-gap:27px;row-gap:20px}
.svc-item{height:108px;background:var(--white);border:1px solid #e6e6e6;display:flex;flex-direction:column;align-items:center;justify-content:center;gap:8px;text-align:center;font-size:14px;line-height:18px}
.btn-solid{left:302px;top:1631px;width:118px;height:43px;background:var(--teal);color:var(--white);border-radius:3px;font-size:11px;font-weight:600;display:flex;align-items:center;justify-content:center}
.svc-art{left:727px;top:1341px;width:388px;height:250px;background:linear-gradient(180deg,#f1f3f3,#e1e9e7 60%,#cddfdb);border-radius:6px}
/* reviews */
.fb-head{left:0;top:1757px;width:1200px;text-align:center}
.fb-head .sec-title{margin-top:8px}
.review-row{display:flex;gap:20px}
.review{flex:0 0 257px;height:169px;background:var(--white);padding:16px 9px 0 9px;position:relative}
.review p{font-size:10px;line-height:15px;color:var(--muted)}
.review .more{font-size:10px;font-weight:600;color:var(--teal);margin-top:7px}
.review .name{position:absolute;left:9px;top:108px;font-family:"Nunito",sans-serif;font-weight:700;font-size:17px}
.review .foot{position:absolute;left:9px;right:9px;top:142px;display:flex;justify-content:space-between;align-items:center}
.review .stars{display:flex;gap:4px}
.review .date{font-size:10px;color:var(--muted)}
/* cta */
.cta{left:0;top:2364px;width:1200px;height:382px;background:var(--teal);text-align:center;color:var(--white)}
.cta h2{margin-top:56px;font-family:"Nunito",sans-serif;font-weight:900;font-size:45px;line-height:44px}
.cta h2 span{color:#e0a22f}
.cta p{margin:20px auto 0;width:385px;font-family:"Montserrat",sans-serif;font-size:16.5px;line-height:20.5px}
.btn-copper{display:inline-flex;margin-top:18px;width:113px;height:38px;background:var(--copper-btn);border-radius:19px;align-items:center;justify-content:center;font-size:11px;font-weight:600}
/* footer */
.foot-brand{left:121px;top:2818px}
.foot-about{left:117px;top:2881px;width:260px;font-size:17px;line-height:22px}
.foot-col h4{font-family:"Nunito",sans-serif;font-weight:700;font-size:17px;margin-bottom:8px}
.foot-col li{list-style:none;font-size:10.5px;line-height:21.5px}
.foot-col p{font-size:10.5px;line-height:15.5px}
.map{left:808px;top:2792px;width:273px;height:140px;background:linear-gradient(135deg,#e9eef0,#d8e4e8 55%,#c3dbe6);border-radius:2px}
.socials{left:937px;top:2966px;display:flex;gap:19px}
.socials span{width:24px;height:24px;border-radius:50%;background:#c9c9c9}
.rule{left:116px;top:3007px;width:965px;height:1px;background:#9a9a9a}
.copyright{left:0;top:3032px;width:1200px;text-align:center;font-size:11px;color:var(--muted)}
</style>
</head>
<body>
<svg width="0" height="0" style="position:absolute">
  <defs>
    <symbol id="star" viewBox="0 0 24 24"><path d="M12 2l2.9 6.6 7.1.6-5.4 4.7 1.6 7L12 17.3 5.8 21l1.6-7L2 9.2l7.1-.6z" fill="#1b8c84"/></symbol>
  </defs>
</svg>

<!-- header -->
<header class="site-header abs">
  <div class="brand"><span class="brand-mark"></span><span class="brand-name">TORVANE</span></div>
  <nav class="main-nav">
    <a style="left:0">Home</a>
    <a style="left:82px">Business Insurance</a>
    <a style="left:264px">Who We Serve</a>
    <a style="left:409px">Risk Management</a>
    <a style="left:582px">Contact Us</a>
  </nav>
</header>

<!-- hero -->
<section class="hero abs">
  <div class="hero-eyebrow abs">Torvane Group</div>
  <h1 class="hero-title abs">Building Your Dreams<br>Into Reality</h1>
  <p class="hero-text abs">Expert Craftsmanship Meets Unmatched Reliability in the Heart of London. Welcome to Torvane Group Where Construction Meets Excellence. Based in London, we are committed to transforming your spaces into exceptional places.</p>
  <a class="btn-outline abs">Learn More</a>
  <div class="hero-art abs" role="img" aria-label="Illustration of three construction workers in teal uniforms in front of a building site"></div>
</section>

<!-- why choose us -->
<svg class="deco-left abs" width="400" height="560" viewBox="0 0 400 560"><circle cx="120" cy="280" r="275" fill="#1b8c84"/></svg>
<svg class="deco-right abs" width="1200" height="700" viewBox="0 0 1200 700"><circle cx="1400" cy="370" r="470" fill="#1b8c84"/></svg>

<div class="why-photo abs" role="img" aria-label="Photograph of a modern glass building against a teal sky"></div>
<div class="stat-box abs">
  <div class="stat-inner">
    <svg width="44" height="32" viewBox="0 0 44 32"><g fill="none" stroke="#fff" stroke-width="2"><path d="M2 30h40"/><rect x="5" y="6" width="8" height="24"/><rect x="17" y="14" width="8" height="16"/><rect x="29" y="2" width="8" height="28"/></g></svg>
    <div class="num">90%<sup>+</sup></div>
    <div class="lbl">already inhabited</div>
  </div>
</div>

<div class="why-head abs">
  <div class="eyebrow">Why Choose Us?</div>
  <h2 class="sec-title">Find Reasons to Choose Us<br>As <em>Your Construction Partner</em></h2>
</div>

<article class="feature-card abs" style="left:554px;top:844px">
  <div class="ico"><svg width="34" height="34" viewBox="0 0 34 34"><g fill="none" stroke="#6a9f9a" stroke-width="1.5"><rect x="3" y="5" width="28" height="24"/><path d="M3 11h28M9 17h8v8H9zM21 17h6M21 21h6M21 25h6"/></g></svg></div>
  <div><h3>Our Expertise</h3><p>Leveraging over 10 years of experience, Torvane Group stands as a beacon of excellence in the construction industry. We handle each project, big or small....</p></div>
</article>
<article class="feature-card abs" style="left:846px;top:844px">
  <div class="ico"><svg width="34" height="34" viewBox="0 0 34 34"><g fill="none" stroke="#6a9f9a" stroke-width="1.5"><path d="M4 16L17 4l13 12M8 13v17h18V13"/><path d="M13 22l3 3 6-7"/></g></svg></div>
  <div><h3>Quality Assurance</h3><p>Quality is not just a promise, but a practice. Meticulous attention to detail ensures flawless finishes and durable structures, bringing long-lasting satisfaction to our clients.</p></div>
</article>
<article class="feature-card abs" style="left:715px;top:1012px">
  <div class="ico"><svg width="34" height="34" viewBox="0 0 34 34"><g fill="none" stroke="#6a9f9a" stroke-width="1.5"><circle cx="17" cy="10" r="5"/><path d="M7 31c0-8 4-13 10-13s10 5 10 13M12 8h10"/></g></svg></div>
  <div><h3>Certified Excellence</h3><p>Your safety and satisfaction are our top priorities. We provide electrical certificates and adhere to the highest industry standards, offering peace of mind in every service.</p></div>
</article>

<!-- services -->
<div class="svc-head abs">
  <div class="eyebrow">Our Services</div>
  <h2 class="sec-title" style="margin-top:4px">We Can Bring Your <em>Vision To Life</em>, Covering<br>Every Aspect Of Construction</h2>
</div>

<div class="svc-grid abs">
  <div class="svc-item"><svg width="32" height="30" viewBox="0 0 32 30"><g fill="none" stroke="#1b8c84" stroke-width="1.4"><rect x="4" y="3" width="24" height="8" rx="2"/><rect x="14" y="14" width="14" height="14"/><path d="M8 11v12h6M19 19l2-3v5l2-3"/></g></svg><span>Electrical<br>Work</span></div>
  <div class="svc-item"><svg width="32" height="30" viewBox="0 0 32 30"><g fill="none" stroke="#1b8c84" stroke-width="1.4"><rect x="7" y="8" width="18" height="19" rx="2"/><path d="M7 8c0-4 18-4 18 0M16 14c-2 3-3 4-3 6a3 3 0 006 0c0-2-1-3-3-6z"/></g></svg><span>Painting &amp;<br>Decoration</span></div>
  <div class="svc-item"><svg width="32" height="30" viewBox="0 0 32 30"><g fill="none" stroke="#1b8c84" stroke-width="1.4"><rect x="9" y="10" width="6" height="18"/><rect x="18" y="14" width="6" height="14"/><path d="M12 10V3M21 14V6"/></g></svg><span>Plastering</span></div>
  <div class="svc-item"><svg width="32" height="30" viewBox="0 0 32 30"><g fill="none" stroke="#1b8c84" stroke-width="1.4"><path d="M4 15L16 4l12 11M8 12v15h16V12"/><path d="M12 20h8v7h-8z"/></g></svg><span>Plumbing</span></div>
  <div class="svc-item"><svg width="32" height="30" viewBox="0 0 32 30"><g fill="none" stroke="#1b8c84" stroke-width="1.4"><path d="M5 6h18v6H5zM23 8h5M10 12v15h5V12"/></g></svg><span>Carpentry</span></div>
  <div class="svc-item"><svg width="32" height="30" viewBox="0 0 32 30"><g fill="none" stroke="#1b8c84" stroke-width="1.4"><path d="M4 17h24M6 17v6a4 4 0 004 4h12a4 4 0 004-4v-6M16 5v8M12 9h8"/></g></svg><span>Kitchen &amp;<br>Bathroom</span></div>
  <div class="svc-item"><svg width="32" height="30" viewBox="0 0 32 30"><g fill="none" stroke="#1b8c84" stroke-width="1.4"><rect x="10" y="3" width="12" height="25"/><path d="M10 10h12M10 17h12M13 22h6"/></g></svg><span>Loft<br>Conversion</span></div>
  <div class="svc-item"><svg width="32" height="30" viewBox="0 0 32 30"><g fill="none" stroke="#1b8c84" stroke-width="1.4"><rect x="4" y="6" width="24" height="18"/><path d="M4 12h24M4 18h24M14 6v6M20 12v6M11 18v6"/></g></svg><span>Extensions</span></div>
</div>
<a class="btn-solid abs">Learn More</a>
<div class="svc-art abs" role="img" aria-label="Illustration of a teal dump truck, excavator and worker on a construction site"></div>

<!-- feedback -->
<div class="fb-head abs">
  <div class="eyebrow">Client Feedback</div>
  <h2 class="sec-title">Our Commitment To <em>Excellence Has Earned Us</em><br><em>The Trust</em> Of Numerous Homeowners And<br>Businesses In London</h2>
</div>

<div class="review-row abs" style="left:52px;top:1931px">
  <div class="review"><p>Lorem ipsum dolor sit amet consectetur. Cursus morbi nisi felis imperdiet diam risus gravida. Imperdiet ac lorem et massa amet malesuada sapien varius non. Tortor arcu in purus blandit.</p><div class="more">Read More</div><div class="name">Tam</div><div class="foot"><div class="stars"><svg width="15" height="15"><use href="#star"/></svg><svg width="15" height="15"><use href="#star"/></svg><svg width="15" height="15"><use href="#star"/></svg><svg width="15" height="15"><use href="#star"/></svg><svg width="15" height="15"><use href="#star"/></svg></div><span class="date">4 days ago</span></div></div>
  <div class="review"><p>Lorem ipsum dolor sit amet consectetur. Lectus facilisi consequat pellentesque amet volutpat est massa velit. Quisque in senectus massa vitae habitasse. Egestas condimentum quisque.</p><div class="name">Brookmere</div><div class="foot"><div class="stars"><svg width="15" height="15"><use href="#star"/></svg><svg width="15" height="15"><use href="#star"/></svg><svg width="15" height="15"><use href="#star"/></svg><svg width="15" height="15"><use href="#star"/></svg><svg width="15" height="15"><use href="#star"/></svg></div><span class="date">4 days ago</span></div></div>
  <div class="review"><p>Lorem ipsum dolor sit amet consectetur. Et ultrices vehicula turpis porta dictum. Ac mollis diam auctor diam egestas sit. Sollicitudin lorem consectetur massa eget at tincidunt non. Nisl.</p><div class="more">Read More</div><div class="name">Neil Ardwick</div><div class="foot"><div class="stars"><svg width="15" height="15"><use href="#star"/></svg><svg width="15" height="15"><use href="#star"/></svg><svg width="15" height="15"><use href="#star"/></svg><svg width="15" height="15"><use href="#star"/></svg><svg width="15" height="15"><use href="#star"/></svg></div><span class="date">6 days ago</span></div></div>
  <div class="review"><p>Lorem ipsum dolor sit amet consectetur. Sem condimentum non eu amet ullamcorper pellentesque auctor. Tincidunt odio at eu.</p><div class="name">Owen Pratt</div><div class="foot"><div class="stars"><svg width="15" height="15"><use href="#star"/></svg><svg width="15" height="15"><use href="#star"/></svg><svg width="15" height="15"><use href="#star"/></svg><svg width="15" height="15"><use href="#star"/></svg><svg width="15" height="15"><use href="#star"/></svg></div><span class="date">6 days ago</span></div></div>
  <div class="review"><p>Lorem ipsum dolor sit amet consectetur. Pretium nibh egestas ut nisl tempus amet dui lectus.</p><div class="name">Leo</div><div class="foot"><div class="stars"><svg width="15" height="15"><use href="#star"/></svg><svg width="15" height="15"><use href="#star"/></svg><svg width="15" height="15"><use href="#star"/></svg><svg width="15" height="15"><use href="#star"/></svg><svg width="15" height="15"><use href="#star"/></svg></div><span class="date">1 week ago</span></div></div>
</div>

<div class="review-row abs" style="left:-46px;top:2116px">
  <div class="review"><p>Lorem ipsum dolor sit amet consectetur. Sed dictum fames nibh nibh varius. Risus mattis mi urna neque placerat dignissim mauris libero. Sed non mollis nullam nisi. Diam.</p><div class="more">Read More</div><div class="name">Ruth</div><div class="foot"><div class="stars"><svg width="15" height="15"><use href="#star"/></svg><svg width="15" height="15"><use href="#star"/></svg><svg width="15" height="15"><use href="#star"/></svg><svg width="15" height="15"><use href="#star"/></svg><svg width="15" height="15"><use href="#star"/></svg></div><span class="date">1 week ago</span></div></div>
  <div class="review"><p>Lorem ipsum dolor sit amet consectetur. Ante facilisis mi luctus aenean sit sed egestas mi ac. At at ut pellentesque in maecenas diam. Vel pulvinar mattis id duis ante lacus porttitor.</p><div class="name">Tam</div><div class="foot"><div class="stars"><svg width="15" height="15"><use href="#star"/></svg><svg width="15" height="15"><use href="#star"/></svg><svg width="15" height="15"><use href="#star"/></svg><svg width="15" height="15"><use href="#star"/></svg><svg width="15" height="15"><use href="#star"/></svg></div><span class="date">November 27</span></div></div>
  <div class="review"><p>Lorem ipsum dolor sit amet consectetur. Cras non eget nunc fames nec nulla mollis amet potenti. Nisl elit auctor dui lacus lorem. Consectetur magna nulla lacinia pellentesque.</p><div class="name">Fiona Ashby</div><div class="foot"><div class="stars"><svg width="15" height="15"><use href="#star"/></svg><svg width="15" height="15"><use href="#star"/></svg><svg width="15" height="15"><use href="#star"/></svg><svg width="15" height="15"><use href="#star"/></svg><svg width="15" height="15"><use href="#star"/></svg></div><span class="date">November 26</span></div></div>
  <div class="review"><p>Lorem ipsum dolor sit amet consectetur. Phasellus nisl tincidunt consectetur massa cras. Pellentesque ut integer quis diam volutpat magna. Aliquet sit diam vitae volutpat nibh.</p><div class="more">Read More</div><div class="name">Kieran Holt</div><div class="foot"><div class="stars"><svg width="15" height="15"><use href="#star"/></svg><svg width="15" height="15"><use href="#star"/></svg><svg width="15" height="15"><use href="#star"/></svg><svg width="15" height="15"><use href="#star"/></svg><svg width="15" height="15"><use href="#star"/></svg></div><span class="date">November 22</span></div></div>
  <div class="review"><p>Lorem ipsum dolor sit amet consectetur. Amet nulla nunc odio leo aenean. Gravida mauris sit urna feugiat tincidunt cursus. Risus quam.</p><div class="more">Read More</div><div class="name">Declan</div><div class="foot"><div class="stars"><svg width="15" height="15"><use href="#star"/></svg><svg width="15" height="15"><use href="#star"/></svg><svg width="15" height="15"><use href="#star"/></svg><svg width="15" height="15"><use href="#star"/></svg><svg width="15" height="15"><use href="#star"/></svg></div><span class="date">November 20</span></div></div>
</div>

<!-- call to action -->
<section class="cta abs">
  <h2><span>Ready to start</span><br>your Project<br>with Us?</h2>
  <p>Contact us today for a consultation and embark on the journey to turn your construction dreams into a stunning reality.</p>
  <a class="btn-copper">Contact Us</a>
</section>

<!-- footer -->
<footer>
  <div class="foot-brand brand abs"><span class="brand-mark"></span><span class="brand-name">TORVANE</span></div>
  <p class="foot-about abs">Lorem ipsum dolor sit amet consectetur. Morbi donec interdum morbi felis. Feugiat aliquam non sem lectus tellus.</p>
  <div class="foot-col abs" style="left:445px;top:2800px">
    <h4>Company</h4>
    <ul><li>About Us</li><li>Services</li><li>Projects</li><li>Contact Uss</li></ul>
  </div>
  <div class="foot-col abs" style="left:620px;top:2800px;width:160px">
    <h4>Contact Info</h4>
    <p>Lorem ipsum dolor sit amet consectetur. Placerat arcu id aliquam proin. Sit massa neque ultricies tincidunt.</p>
    <p style="margin-top:10px">+3xx x xxx xxxx</p>
    <p style="margin-top:10px">info@torvanegroup.co.uk</p>
  </div>
  <div class="map abs" role="img" aria-label="Map of central London showing the company location"></div>
  <div class="socials abs"><span></span><span></span><span></span><span></span></div>
  <div class="rule abs"></div>
  <div class="copyright abs">© 2024 Torvane Group. All Rights Reserved.</div>
</footer>
</body>
</html>
```